依頼詳細
新聞折込用のB4チラシの作成をお願いいたします。

9月20日の敬老の日に向けて、使用予定です。
・50〜60代向け
・健康的なイメージ
・写真をいれてほしい
(セラピストの写真は提供いたします。受け手が若い女性なので、受け手の顔を隠す・施術写真とは別に50〜60代の方の写真を入れるなどご対応お願いします。)

裏面は既存のデザインを利用予定のため、表面の作成をお願いいたします。
裏面のデザインを添付しますのでご参考していただけると幸いです。
https://48.parcelbox.jp/0913-8a27c5d1e9b04f36a2e8d71c5f0b94ae

ウェブでの展開も検討しておりますので、aiデータでいただきたいです。
記載項目
①「肩のお疲れ」「足腰のお疲れ」などお疲れの部位に訴えかけるワード

②「50代以上の方 限定クーポン」
1)60分以上のコース1,000円引き
2)平日はさらにお得!60分以上のコース1,500円引き

③治療目的ではないため保険は適用されません。の記載

④9月以外での利用も検討しているため、「敬老の日」という文言は不要です。

NGワード
・肩こり
・腰痛
・むくみ
リラクゼーションのため、具体的症状や治療を連想させる文言はいれないようお願いいたします。
サイズ
B4
ページ数
片面
希望イメージ
シンプル 複雑
単色 カラフル
暗い 明るい
日常 高級
遊び心 厳粛
未来的 伝統的
女性的 男性的
希望する色
ブランドカラーは緑ですが、こだわり過ぎず
納品ファイル
• イラストレーター形式 (.ai)
補足説明
■ 選んだ理由

こちらのターゲット設定に対して、イメージと近いものでした。
普段のブランドでは出さない雰囲気で、試してみたいと思いました。

■ 提案者全員のお礼・コメント

ご応募いただきありがとうございました。
活用させていただきます。

```html
<!DOCTYPE html>
<html lang="ja">
<head>
<meta charset="utf-8">
<title>50代以上の方限定 割引キャンペーン</title>
<link rel="stylesheet" href="https://fonts.googleapis.com/css2?family=Noto+Sans+JP:wght@400;500;700;900&display=swap">
<style>
  :root{
    --red:#d8203a;
    --ink:#1d1d1d;
    --green:#4ea63c;
    --green-dark:#2f7f2a;
    --leaf:#8cc63f;
    --yellow:#fff08a;
    --yellow-deep:#f5d800;
    --paper:#ffffff;
    --soft:#f4f9ee;
  }
  *{margin:0;padding:0;box-sizing:border-box;}
  html,body{width:865px;height:1200px;overflow:hidden;background:var(--paper);}
  body{font-family:"Noto Sans JP",sans-serif;color:var(--ink);position:relative;}
  .flyer{position:absolute;inset:0;background:linear-gradient(180deg,var(--soft) 0%,#fff 30%,#fff 100%);}
  .trim-label{position:absolute;left:8px;top:6px;font-size:11px;color:#555;}
  .leaves-left,.leaves-right{position:absolute;top:0;}
  .leaves-left{left:0;width:200px;height:150px;background:radial-gradient(ellipse at 0 0,var(--leaf) 0%,rgba(140,198,63,.5) 45%,rgba(140,198,63,0) 72%);}
  .leaves-right{right:0;width:240px;height:170px;background:radial-gradient(ellipse at 100% 0,var(--leaf) 0%,rgba(140,198,63,.5) 45%,rgba(140,198,63,0) 72%);}

  .headline{position:absolute;font-weight:900;line-height:1;white-space:nowrap;}
  .headline-age{left:120px;top:48px;font-size:132px;color:var(--red);letter-spacing:2px;
    -webkit-text-stroke:0;text-shadow:0 0 0 #fff,4px 4px 0 #fff,-4px -4px 0 #fff,4px -4px 0 #fff,-4px 4px 0 #fff,6px 8px 10px rgba(0,0,0,.25);}
  .headline-limited{left:468px;top:184px;font-size:62px;color:var(--ink);}
  .headline-discount{left:70px;top:180px;font-size:118px;color:var(--red);
    text-shadow:4px 4px 0 #fff,-4px -4px 0 #fff,4px -4px 0 #fff,-4px 4px 0 #fff,6px 8px 10px rgba(0,0,0,.25);}
  .headline-campaign{left:322px;top:252px;font-size:55px;color:var(--ink);}
  .bring-note{position:absolute;left:520px;top:318px;font-size:13px;font-weight:500;}
  .bring-note .star{color:var(--yellow-deep);}

  .photo{position:absolute;background:linear-gradient(160deg,#e9d6c4,#c9b29c);}
  .photo-senior-a{left:62px;top:340px;width:130px;height:140px;border-radius:50%;}
  .photo-senior-b{left:178px;top:332px;width:140px;height:150px;border-radius:50%;background:linear-gradient(160deg,#e3dcd2,#b9aa98);}
  .photo-senior-c{left:300px;top:336px;width:140px;height:146px;border-radius:50%;background:linear-gradient(160deg,#d7e2d8,#9db39d);}
  .photo-treatment{right:0;top:330px;width:440px;height:660px;background:linear-gradient(180deg,rgba(255,255,255,0) 0%,#e8efe0 20%,#d9c8b4 60%,#c6d8b8 100%);
    -webkit-mask:linear-gradient(90deg,transparent 0,#000 18%);mask:linear-gradient(90deg,transparent 0,#000 18%);}

  .coupon{position:absolute;left:58px;top:488px;width:382px;background:#fff;border:3px solid var(--yellow-deep);border-radius:6px;padding:12px 14px;box-shadow:0 3px 8px rgba(0,0,0,.15);}
  .coupon-row{display:flex;align-items:baseline;gap:8px;font-weight:700;white-space:nowrap;}
  .coupon-course{font-size:21px;}
  .coupon-price{font-size:36px;color:var(--red);font-weight:900;}
  .coupon-price small{font-size:24px;}
  .coupon-weekday{display:inline-block;margin:6px 0 2px;font-size:19px;font-weight:700;color:#2a6ab3;background:var(--yellow);padding:0 6px;}
  .coupon-row.highlight{background:var(--yellow);margin:0 -14px -12px;padding:2px 14px 8px;}

  .appeal{position:absolute;left:52px;top:676px;font-weight:900;line-height:1.18;white-space:nowrap;}
  .appeal-parts{font-size:60px;}
  .appeal-ease{font-size:64px;background:linear-gradient(transparent 62%,var(--yellow) 62%);}
  .appeal-reset{font-size:56px;margin-top:4px;}

  .consult-bubble{position:absolute;left:410px;top:664px;width:134px;height:134px;border-radius:50%;background:var(--yellow);border:3px solid #fff;box-shadow:0 3px 8px rgba(0,0,0,.2);
    display:flex;align-items:center;justify-content:center;text-align:center;font-size:19px;font-weight:700;line-height:1.3;transform:rotate(8deg);}
  .insurance-note{position:absolute;left:56px;top:924px;font-size:11px;color:#444;}

  .brand-band{position:absolute;left:0;right:0;bottom:0;height:215px;background:linear-gradient(180deg,rgba(78,166,60,0) 0%,var(--green) 30%,var(--green-dark) 100%);
    display:flex;align-items:center;justify-content:center;gap:14px;padding-top:40px;}
  .brand-dot{width:14px;height:14px;border-radius:50%;background:#fff;}
  .brand-name{font-size:54px;font-weight:700;color:#fff;letter-spacing:4px;}
</style>
</head>
<body>
<main class="flyer">
  <p class="trim-label">サイズ B4｜257×364mm</p>
  <div class="leaves-left" role="img" aria-label="緑の葉のあしらい"></div>
  <div class="leaves-right" role="img" aria-label="緑の葉のあしらい"></div>

  <h1>
    <span class="headline headline-age">50代以上</span>
    <span class="headline headline-limited">の方限定</span>
    <span class="headline headline-discount">割引</span>
    <span class="headline headline-campaign">キャンペーン</span>
  </h1>
  <p class="bring-note"><span class="star">★</span>こちらのチラシをご持参ください。</p>

  <div class="photo photo-senior-a" role="img" aria-label="首に手を当てる50代女性の写真"></div>
  <div class="photo photo-senior-b" role="img" aria-label="肩を押さえる60代男性の写真"></div>
  <div class="photo photo-senior-c" role="img" aria-label="腰に手を当てる人物の写真"></div>
  <div class="photo photo-treatment" role="img" aria-label="セラピストが背中をほぐす施術の写真"></div>

  <section class="coupon">
    <div class="coupon-row"><span class="coupon-course">60分以上のコース</span><span class="coupon-price">1,000<small>円引き</small></span></div>
    <span class="coupon-weekday">★平日はさらにお得!</span>
    <div class="coupon-row highlight"><span class="coupon-course">60分以上のコース</span><span class="coupon-price">1,500<small>円引き</small></span></div>
  </section>

  <section class="appeal">
    <p class="appeal-parts">首・肩・腰の</p>
    <p><span class="appeal-ease">疲れをラクに!</span></p>
    <p class="appeal-reset">日頃の疲れをリセット</p>
  </section>
  <div class="consult-bubble">お気軽に<br>ご相談<br>ください!</div>
  <p class="insurance-note">※治療目的ではないため保険は適用されません。</p>

  <footer class="brand-band">
    <span class="brand-dot"></span>
    <span class="brand-name">Honoka Rest</span>
  </footer>
</main>
</body>
</html>
```